Eneginering consultancy brochure style web design project

Looking for a new brochure style web page for our small engineering consultancy. The prupose of the website is to provide some basic information with about the company, including exampels of our work, and present a way to initiate contact. There there will only be a few pages (up to 5) and limited content.A main focus of the project is to develop the visual design/identity for the webpage, and to provide the template for us to add content, rearrange layout and modify pages with relative ease.A mixture of text and images will be used. The use of an image slider would be desirable.We have recently had a new company logo developed (uploaded), which defines the colour scheme for the page.A professional. clean look is desired, that is not cluttered and easy to navigate.Template to add a photo slider is desirable.The use of swirl patterns (suach as those used here: https://www.brightvortex.co.uk/) and/or contoured mesh pattern (example attached) within the page is likely to be attractive, as this is in harmony with our activities.

Target Market(s)

Engineering; manufacturing

Industry/Entity Type

Engineering Consultant

Coding

Coded - Design and coding required

Number of Pages Required

3 page

Font styles to use
Other font styles liked:
• Helvetica

Colors
00a990
33b8a4
86cfc6
606060
3176b5
0255a3
85acd3
474747
7f7f7f

Requirements
Must have
• 1) Landing page for information about the company. Mostly text, with image slider.
• 2) One page for example projects. Images with accompanying texts.
• 3) Enquiry/'get in touch' page.
• Simple, uncluttered look and feel.

```html
<!DOCTYPE html>
<html lang="en">
<head>
<meta charset="utf-8">
<title>Ferrow Thermal Systems</title>
<link href="https://fonts.googleapis.com/css2?family=Alegreya:wght@400;500;700&family=Poppins:wght@400;500;600&display=swap" rel="stylesheet">
<style>
:root{
  --teal:#1aa6c2;
  --teal-dark:#0f7a8c;
  --blue:#0255a3;
  --blue-bright:#0a5cf0;
  --cyan:#12c6e6;
  --ink:#222;
  --grey:#474747;
  --grey-mid:#606060;
  --grey-light:#7f7f7f;
  --line:#85acd3;
  --white:#fff;
  --pink:#e8336b;
  --hero-dark:#06313a;
  --hero-mid:#0d5a66;
  --slider-dark:#0a1b4d;
  --slider-mid:#1a3a7a;
}
*{box-sizing:border-box;margin:0;padding:0}
html,body{width:1200px;height:4604px;overflow:hidden}
body{position:relative;font-family:"Poppins",Helvetica,Arial,sans-serif;color:var(--ink);background:var(--white)}
.abs{position:absolute}

/* header */
.site-header{position:absolute;left:0;top:0;width:1200px;height:102px;background:var(--white)}
.brand{position:absolute;display:flex;align-items:center;gap:12px;font-family:"Poppins",sans-serif;font-weight:600;color:var(--blue);font-size:22px;white-space:nowrap}
.brand-dot{width:18px;height:18px;border-radius:50%;background:var(--teal)}
.site-header .brand{left:117px;top:34px}
.main-nav{position:absolute;right:30px;top:44px;display:flex;gap:22px;font-size:13px;color:var(--grey-mid)}

/* hero */
.hero{position:absolute;left:0;top:102px;width:1200px;height:666px;
  background:radial-gradient(ellipse at 70% 55%,#1d8a96 0%,var(--hero-mid) 35%,var(--hero-dark) 80%)}
.hero-title{position:absolute;left:120px;top:128px;width:470px;font-family:"Alegreya",serif;font-weight:500;font-size:47px;line-height:1.2;color:var(--white)}
.hero-text{position:absolute;left:120px;top:355px;width:440px;font-size:16px;line-height:1.3;color:var(--white)}
.btn{display:inline-block;border-radius:24px;background:var(--teal);color:var(--white);font-weight:600;letter-spacing:2px;text-align:center}
.hero .btn{position:absolute;left:120px;top:444px;width:188px;height:44px;line-height:44px;font-size:17px}
.contact-card{position:absolute;left:648px;top:55px;width:411px;height:460px;background:var(--white);padding:44px 36px 0 36px}
.contact-card h2{font-family:"Alegreya",serif;font-weight:700;font-size:24px;line-height:1.25;color:var(--ink);margin-bottom:20px}
.field{height:49px;border:1px solid #e2e2e2;margin-bottom:16px;padding:0 14px;line-height:47px;font-size:15px;color:var(--grey-light)}
.contact-card .btn{position:absolute;right:36px;top:380px;width:104px;height:34px;line-height:34px;font-size:13px;letter-spacing:1.5px}

/* services */
.section-title{position:absolute;left:0;width:1200px;text-align:center;font-weight:500;font-size:34px;color:var(--ink)}
.services-title{top:876px}
.services-intro{position:absolute;left:0;top:936px;width:1200px;text-align:center;font-size:15px;line-height:1.6;color:var(--grey-mid)}
.service{position:absolute;width:290px}
.service svg{display:block;margin-bottom:22px}
.service h3{font-size:17px;font-weight:600;margin-bottom:10px}
.service p{font-size:13.5px;line-height:1.6;color:var(--grey-mid)}

/* slider */
.slider{position:absolute;left:0;top:1526px;width:1200px;height:731px;
  background:radial-gradient(ellipse at 45% 50%,var(--slider-mid) 0%,#132a66 45%,var(--slider-dark) 100%)}
.slider-label{position:absolute;left:0;top:130px;width:1200px;text-align:center;font-family:"Alegreya",serif;font-size:38px;color:#dfe7f5}
.slider-dots{position:absolute;left:578px;top:690px;display:flex;gap:8px}
.slider-dots span{width:8px;height:8px;border-radius:50%;background:rgba(255,255,255,.45)}
.slider-dots span:first-child{background:var(--white)}

/* blog */
.blog-title{position:absolute;left:0;top:2350px;width:1200px;text-align:center;font-family:"Alegreya",serif;font-weight:500;font-size:82px;color:var(--grey)}
.blog-rule{position:absolute;left:368px;top:2455px;width:461px;height:3px;background:var(--line)}
.post{position:absolute;width:288px;background:var(--white);box-shadow:0 2px 12px rgba(0,0,0,.14)}
.post-media{height:176px}
.post-body{padding:22px 18px 20px}
.post h3{font-size:16px;font-weight:600;line-height:1.45;margin-bottom:12px}
.post .byline{font-size:14px;color:var(--grey-light);margin-bottom:12px}
.post p{font-size:14px;line-height:1.62;color:var(--grey-mid)}

/* subscribe */
.sub-count{position:absolute;left:0;top:3240px;width:1200px;text-align:center;font-weight:500;font-size:76px;color:var(--ink)}
.sub-label{position:absolute;left:0;top:3372px;width:1200px;text-align:center;font-size:15px;letter-spacing:3px;color:var(--grey)}
.sub-field{position:absolute;left:375px;top:3448px;width:454px;height:52px;border:1px solid #ddd;padding:0 14px;line-height:50px;font-size:14px;color:var(--grey-light);background:var(--white)}
.sub-btn{position:absolute;left:375px;top:3500px;width:454px;height:44px;line-height:44px;background:var(--teal-dark);color:var(--white);text-align:center;font-size:12px;font-weight:600;letter-spacing:1.5px}

/* overview */
.overview{position:absolute;left:0;top:3647px;width:1200px;height:713px;overflow:hidden;
  background:linear-gradient(100deg,var(--cyan) 0%,#0aa0f0 40%,var(--blue-bright) 100%)}
.overview-title{top:105px;color:var(--white)}
.fact{position:absolute;width:460px;color:var(--white)}
.fact h4{font-size:18px;font-weight:500;margin-bottom:10px}
.fact p{font-size:14px;line-height:1.6;color:rgba(255,255,255,.85)}

/* footer */
.site-footer{position:absolute;left:0;top:4360px;width:1200px;height:244px;background:var(--white)}
.foot-col{position:absolute;top:36px}
.foot-col h5{font-size:18px;font-weight:600;margin-bottom:14px}
.foot-col li{list-style:none;font-size:14px;color:var(--grey-mid);margin-bottom:24px}
.social{display:flex;gap:10px;justify-content:center}
.social span{width:30px;height:30px;background:var(--pink)}
.site-footer .brand{left:0;width:1200px;justify-content:center;top:160px;font-size:20px;gap:10px}
.site-footer .brand-dot{width:16px;height:16px}
</style>
</head>
<body>

<header class="site-header">
  <div class="brand"><span class="brand-dot"></span>Ferrow Thermal Systems</div>
  <nav class="main-nav"><span>Link</span><span>Link</span><span>Link</span><span>Link</span></nav>
</header>

<section class="hero" role="img" aria-label="Dark teal background with a glowing contoured digital mesh wave">
  <h1 class="hero-title">Engineering built to meet the needs of your business.</h1>
  <p class="hero-text">Ut porttitor imperdiet hendrerit. Suspendisse pulvinar lacus nec sollicitudin finibus ligula quam bibendum dui, maximus ornare ex nulla ut lacus.</p>
  <span class="btn">LEARN MORE</span>
  <form class="contact-card">
    <h2>Get in touch so we can help your company!</h2>
    <div class="field">Your Name</div>
    <div class="field">Email Address</div>
    <div class="field">Company Name</div>
    <div class="field">Website</div>
    <span class="btn">SUBMIT</span>
  </form>
</section>

<section class="services">
  <h2 class="section-title services-title">Our Services</h2>
  <p class="services-intro">Lorem ipsum dolor sit amet, consectetur adipiscing elit.<br>Pellentesque imperdiet libero eu neque facilisis.</p>

  <div class="service" style="left:117px;top:1050px">
    <svg width="40" height="34" viewBox="0 0 40 34" fill="none" stroke="#1aa6c2" stroke-width="1.8"><rect x="4" y="18" width="8" height="12"/><rect x="14" y="12" width="8" height="18"/><rect x="24" y="6" width="8" height="24"/><line x1="1" y1="31" x2="38" y2="31"/></svg>
    <h3>Specialty</h3><p>In luctus aliquam nibh a pretium. Morbi auctor a mauris ac accumsan.</p>
  </div>
  <div class="service" style="left:455px;top:1050px">
    <svg width="40" height="34" viewBox="0 0 40 34" fill="none" stroke="#1aa6c2" stroke-width="1.8"><rect x="4" y="4" width="24" height="26"/><line x1="9" y1="12" x2="22" y2="12"/><line x1="9" y1="18" x2="22" y2="18"/><line x1="9" y1="24" x2="18" y2="24"/><path d="M24 22 L36 8 L38 10 L26 24 Z"/></svg>
    <h3>Specialty</h3><p>In luctus aliquam nibh a pretium. Morbi auctor a mauris ac accumsan.</p>
  </div>
  <div class="service" style="left:792px;top:1050px">
    <svg width="40" height="34" viewBox="0 0 40 34" fill="none" stroke="#1aa6c2" stroke-width="1.8"><path d="M20 30 C12 20 10 16 10 12 A10 10 0 0 1 30 12 C30 16 28 20 20 30 Z"/><circle cx="20" cy="12" r="4"/></svg>
    <h3>Specialty</h3><p>In luctus aliquam nibh a pretium. Morbi auctor a mauris ac accumsan.</p>
  </div>
  <div class="service" style="left:117px;top:1258px">
    <svg width="40" height="34" viewBox="0 0 40 34" fill="none" stroke="#1aa6c2" stroke-width="1.8"><circle cx="18" cy="18" r="13"/><path d="M18 5 V18 H31"/><path d="M22 2 A14 14 0 0 1 34 14 H22 Z"/></svg>
    <h3>Specialty</h3><p>In luctus aliquam nibh a pretium. Morbi auctor a mauris ac accumsan.</p>
  </div>
  <div class="service" style="left:455px;top:1258px">
    <svg width="40" height="34" viewBox="0 0 40 34" fill="none" stroke="#1aa6c2" stroke-width="1.8"><path d="M8 2 H26 L32 8 V32 H8 Z"/><polyline points="12,24 17,18 21,21 28,13"/></svg>
    <h3>Specialty</h3><p>In luctus aliquam nibh a pretium. Morbi auctor a mauris ac accumsan.</p>
  </div>
  <div class="service" style="left:792px;top:1258px">
    <svg width="40" height="34" viewBox="0 0 40 34" fill="none" stroke="#1aa6c2" stroke-width="1.8"><rect x="8" y="2" width="22" height="30"/><line x1="12" y1="9" x2="26" y2="9"/><line x1="12" y1="15" x2="26" y2="15"/><line x1="12" y1="21" x2="26" y2="21"/><line x1="12" y1="27" x2="20" y2="27"/></svg>
    <h3>Specialty</h3><p>In luctus aliquam nibh a pretium. Morbi auctor a mauris ac accumsan.</p>
  </div>
</section>

<section class="slider" role="img" aria-label="Slider photo of an engineer working with wiring under deep blue light">
  <div class="slider-label">Slider</div>
  <div class="slider-dots"><span></span><span></span><span></span></div>
</section>

<section class="blog">
  <h2 class="blog-title">Our Blog</h2>
  <div class="blog-rule"></div>

  <article class="post" style="left:117px;top:2557px">
    <div class="post-media" role="img" aria-label="Colourful painted artwork on a wall" style="background:linear-gradient(135deg,#c9a27c,#a04a32 55%,#3b4a6a)"></div>
    <div class="post-body">
      <h3>What it Means to Strategize and Globalize a Growing Brand During Acquisitions</h3>
      <div class="byline">by Nora Vance</div>
      <p>AKA: Not as hard as being a single mom/full-time employee/full-time college student, but pretty darn hard. My job as Director, Creative &amp; Brand at Brightfold wears a lot of hats. I regularly function as a brand strategist, project manager, workflow consultant,...</p>
    </div>
  </article>

  <article class="post" style="left:455px;top:2557px">
    <div class="post-media" role="img" aria-label="Desk with a notebook and a framed quote" style="background:linear-gradient(135deg,#f1efe9,#d9d5cc 60%,#b9b3a6)"></div>
    <div class="post-body">
      <h3>What tips would you recommend to a first-time manager?</h3>
      <div class="byline">by Nora Vance</div>
      <p>I got this question today, and I've been thinking about this a lot. When we enter management for the first time, it can be overwhelming. Much in the way that entering parenthood is intimidating and sudden.</p>
    </div>
  </article>

  <article class="post" style="left:792px;top:2557px">
    <div class="post-media" role="img" aria-label="Dark event banner for a leadership summit" style="background:linear-gradient(135deg,#2a1f2c,#120d16)"></div>
    <div class="post-body">
      <h3>Reflections on Rising Leaders Summit</h3>
      <div class="byline">by Nora Vance</div>
      <p>Rising Leaders Summit took place the weekend of September 30 in Harborview. Daniel and I couldn't both be away from the kids, so I asked my girlfriend/an exchange-listed company's budding entrepreneur Mara to go up with me. First of all, we had SO much fun! It was an absolute blast and so nice to get a little bit of girl time with a good friend with lots of conversation with interesting young humans.</p>
    </div>
  </article>
</section>

<svg class="abs" style="left:0;top:3330px" width="380" height="520" viewBox="0 0 380 520" aria-hidden="true">
  <circle cx="150" cy="230" r="230" fill="#12c6d8"/>
</svg>

<section class="subscribe">
  <div class="sub-count">2,000+</div>
  <div class="sub-label">SUBSCRIBERS</div>
  <div class="sub-field">Email</div>
  <div class="sub-btn">SUBSCRIBE</div>
</section>

<section class="overview">
  <svg class="abs" style="left:0;top:0" width="300" height="713" viewBox="0 0 300 713" aria-hidden="true">
    <circle cx="138" cy="-87" r="230" fill="#12c6d8"/>
    <path d="M0 300 C80 340 120 420 110 520 C105 580 70 620 30 640 L0 650 Z" fill="rgba(180,230,255,.35)"/>
  </svg>
  <h2 class="section-title overview-title">Overview of the Company</h2>
  <div class="fact" style="left:123px;top:224px"><h4>Fact 1</h4><p>Proin maximus viverra elit. Vivamus vehicula arcu sed nibh vestibulum lacinia. Fusce vitae viverra risus. Mauris molestie vitae erat quis interdum.</p></div>
  <div class="fact" style="left:123px;top:366px"><h4>Fact 2</h4><p>Etiam in turpis auctor, dignissim tellus eu, molestie elit. Nam dapibus vitae lacus non sodales. Phasellus pretium quam vitae dui viverra placerat.</p></div>
  <div class="fact" style="left:123px;top:508px"><h4>Fact 3</h4><p>Proin maximus viverra elit. Vivamus vehicula arcu sed nibh vestibulum lacinia. Fusce vitae viverra risus. Mauris molestie vitae erat quis interdum.</p></div>
  <div class="fact" style="left:626px;top:224px"><h4>Fact 4</h4><p>Aliquam erat volutpat. Aliquam euismod massa et, sed fermentum nunc scelerisque vitae. Duis rhoncus scelerisque aliquet. Duis vehicula nunc a elementum facilisis. Etiam in turpis auctor, dignissim tellus eu, molestie elit. Nam dapibus vitae lacus non sodales. Phasellus pretium quam vitae dui viverra placerat. Nulla quis justo eget odio elementum porta non ac dui. Fusce quis ultrices eros, in commodo dolor.</p></div>
  <div class="fact" style="left:626px;top:436px"><h4>Fact 5</h4><p>Proin maximus viverra elit. Vivamus vehicula arcu sed nibh vestibulum lacinia. Fusce vitae viverra risus. Mauris molestie vitae erat quis interd.</p></div>
</section>

<footer class="site-footer">
  <div class="foot-col" style="left:117px">
    <h5>Location</h5>
    <ul><li>Address Line 1</li><li>Line 2</li><li>City State</li></ul>
  </div>
  <div class="foot-col" style="left:520px;width:160px;text-align:center">
    <h5>Social Media</h5>
    <div class="social"><span></span><span></span><span></span></div>
  </div>
  <div class="foot-col" style="left:795px">
    <h5>Phone and Email</h5>
    <ul><li>Phone #</li><li>Fax #</li><li>Email Address</li></ul>
  </div>
  <div class="brand"><span class="brand-dot"></span>Ferrow Thermal Systems</div>
</footer>

</body>
</html>
```